Studying Effectively To Do List

I am looking to design a new "Study To Do List" for High School students (Ages 15 - 18) . This will be printed as an A4 notepad and so should only be a single A4 page.

The Design will need to be professional and look semi-serious but also be appealing to High school students (Ages 15 - 18) and should NOT be gender specific.

I have attached a word document outlining the structure of the page. The space provided should be large enough that people can write in it comfortably.

The notepad will most likely be printed in black and white but I'm also looking at coloured options - colours should be kept to a minimum.

This will be printed professionally and should also include a 3mm bleed.

The design should also include the business logo (included in the word document)

Target Market(s)

High School students (Ages 15 - 18). Both genders

Industry/Entity Type

Education

Font styles to use
Serif
Sans Serif

Requirements
Must have
• Please see the word document attached.
Should not have
• Too much colour

```html
<!DOCTYPE html>
<html lang="en">
<head>
<meta charset="utf-8">
<title>Let's Do This – Study Planner</title>
<link href="https://fonts.googleapis.com/css2?family=Playfair+Display:wght@700;800&family=Tinos:wght@700&display=swap" rel="stylesheet">
<style>
  :root {
    --ink: #1a1a1a;
    --rule: #8c8c8c;
    --rule-dark: #333333;
    --paper: #ffffff;
    --box-fill: #ffffff;
    --check: #444444;
  }
  * { box-sizing: border-box; margin: 0; padding: 0; }
  html, body { width: 1200px; height: 848px; overflow: hidden; background: var(--paper); }
  body { position: relative; color: var(--ink); font-family: "Tinos", "Times New Roman", serif; font-weight: 700; }

  .label { font-family: "Tinos", "Times New Roman", serif; font-weight: 700; font-size: 11px; letter-spacing: .2px; text-transform: uppercase; }
  .heading { font-family: "Playfair Display", Georgia, serif; font-weight: 800; text-transform: uppercase; }

  /* ---------- Title ribbon ---------- */
  .title-ribbon { position: absolute; left: 594px; top: 16px; width: 400px; height: 86px; }
  .title-ribbon svg { position: absolute; inset: 0; }
  .title-ribbon .heading { position: absolute; left: 0; right: 0; top: 22px; text-align: center; font-size: 27px; letter-spacing: -.5px; }

  /* ---------- Date tab ---------- */
  .date-tab { position: absolute; left: 1018px; top: 18px; width: 182px; height: 30px; }
  .date-tab svg { position: absolute; inset: 0; }
  .date-tab .label { position: absolute; left: 26px; top: 9px; font-size: 12px; }

  /* ---------- Left panels ---------- */
  .panel { position: absolute; border: 1.5px solid var(--ink); background: var(--box-fill); }
  .panel-tab { position: absolute; left: 4px; top: -1px; height: 32px; border: 1.5px solid var(--ink); background: var(--paper); padding: 7px 6px 0; font-size: 13px; }
  .panel-tab::after { content: ""; position: absolute; right: -10px; top: -1.5px; border-top: 1.5px solid var(--ink); width: 10px; transform: skewY(-20deg); transform-origin: left; }

  .revision { left: 17px; top: 31px; width: 374px; height: 113px; }
  .revision .panel-tab { width: 94px; }
  .rev-item { position: absolute; display: flex; align-items: flex-end; font-size: 11px; height: 14px; }
  .rev-item .num { width: 22px; }
  .rev-item .rule { border-bottom: 1px solid var(--rule-dark); height: 11px; }

  .practice { left: 17px; top: 159px; width: 374px; height: 119px; }
  .practice .panel-tab { width: 92px; }
  .practice .rule { position: absolute; border-bottom: 1px solid var(--rule-dark); }

  .notes { left: 17px; top: 304px; width: 374px; height: 524px; }
  .notes-ribbon { position: absolute; left: 116px; top: 282px; width: 168px; height: 38px; }
  .notes-ribbon svg { position: absolute; inset: 0; }
  .notes-ribbon .heading { position: absolute; left: 0; right: 0; top: 8px; text-align: center; font-size: 14px; font-family: "Tinos", serif; font-weight: 700; }

  /* ---------- Dashed columns ---------- */
  .column { position: absolute; top: 113px; height: 717px; border: 1.5px dashed var(--ink); }
  .homework { left: 403px; width: 385px; }
  .assessments { left: 800px; width: 391px; }
  .column-tab { position: absolute; left: -8px; top: 0; height: 30px; display: flex; align-items: center; padding-left: 10px; font-size: 13px; }
  .column-tab svg { position: absolute; inset: 0; }
  .column-tab span { position: relative; }
  .homework .column-tab { width: 112px; }
  .assessments .column-tab { width: 96px; }

  .checkbox { display: inline-block; width: 15px; height: 15px; border: 1.5px solid var(--check); flex: none; }

  /* homework entries */
  .hw-list { position: absolute; left: 10px; right: 10px; top: 39px; }
  .hw-entry { height: 96px; position: relative; }
  .hw-entry .row { display: flex; align-items: center; gap: 8px; }
  .hw-entry .line { position: absolute; left: 27px; right: 0; border-bottom: 1px solid var(--rule); }
  .hw-entry .task { position: absolute; left: 27px; top: 43px; }

  /* assessment entries */
  .as-list { position: absolute; left: 10px; right: 14px; top: 39px; }
  .as-entry { height: 67.6px; position: relative; }
  .as-entry .row { display: flex; align-items: flex-end; gap: 8px; }
  .as-entry .fill { flex: 1; border-bottom: 1px solid var(--rule-dark); height: 11px; margin: 0 2px; }
  .as-entry .element { position: absolute; left: 23px; top: 14px; }
  .as-entry .line { position: absolute; left: 23px; right: 0; border-bottom: 1px solid var(--rule); }
</style>
</head>
<body>

  <!-- Title ribbon -->
  <div class="title-ribbon">
    <svg viewBox="0 0 400 86" fill="none" stroke="#1a1a1a" stroke-width="1.5">
      <path d="M92 36 H20 L4 18 M4 82 L28 60 L4 44" />
      <path d="M4 82 H92" />
      <path d="M92 60 L110 70 V50" />
      <path d="M308 36 H380 L396 18 M396 82 L372 60 L396 44" />
      <path d="M396 82 H308" />
      <path d="M308 60 L290 70 V50" />
      <rect x="92" y="8" width="216" height="52" rx="8" fill="#fff" />
    </svg>
    <div class="heading">Let's Do This</div>
  </div>

  <!-- Date -->
  <div class="date-tab">
    <svg viewBox="0 0 182 30" fill="none" stroke="#1a1a1a" stroke-width="1.5">
      <path d="M182 1 H2 L18 15 L2 29 H182" />
    </svg>
    <div class="label">Date. __/__/____</div>
  </div>

  <!-- Revision -->
  <section class="panel revision">
    <div class="panel-tab heading">Revision</div>
    <div class="rev-item label" style="left:4px;top:61px"><span class="num">1.)</span><span class="rule" style="width:160px"></span></div>
    <div class="rev-item label" style="left:4px;top:76px"><span class="num">2.)</span><span class="rule" style="width:160px"></span></div>
    <div class="rev-item label" style="left:4px;top:91px"><span class="num">3.)</span><span class="rule" style="width:160px"></span></div>
    <div class="rev-item label" style="left:190px;top:14px"><span class="num">4.)</span><span class="rule" style="width:160px"></span></div>
    <div class="rev-item label" style="left:190px;top:29px"><span class="num">5.)</span><span class="rule" style="width:160px"></span></div>
    <div class="rev-item label" style="left:190px;top:45px"><span class="num">6.)</span><span class="rule" style="width:160px"></span></div>
    <div class="rev-item label" style="left:190px;top:61px"><span class="num">7.)</span><span class="rule" style="width:160px"></span></div>
    <div class="rev-item label" style="left:190px;top:76px"><span class="num">8.)</span><span class="rule" style="width:160px"></span></div>
  </section>

  <!-- Practice -->
  <section class="panel practice">
    <div class="panel-tab heading">Practice</div>
    <div class="rule" style="left:105px;right:24px;top:24px"></div>
    <div class="rule" style="left:105px;right:24px;top:39px"></div>
    <div class="rule" style="left:6px;right:24px;top:57px"></div>
    <div class="rule" style="left:6px;right:24px;top:74px"></div>
    <div class="rule" style="left:6px;right:24px;top:89px"></div>
    <div class="rule" style="left:6px;right:24px;top:104px"></div>
  </section>

  <!-- Notes -->
  <section class="panel notes"></section>
  <div class="notes-ribbon">
    <svg viewBox="0 0 168 38" fill="none" stroke="#1a1a1a" stroke-width="1.5">
      <path d="M28 10 H2 L14 22 L2 34 H34 V26" />
      <path d="M140 10 H166 L154 22 L166 34 H134 V26" />
      <rect x="28" y="2" width="112" height="24" fill="#fff" />
    </svg>
    <div class="heading">Notes</div>
  </div>

  <!-- Homework -->
  <section class="column homework">
    <div class="column-tab label">
      <svg viewBox="0 0 112 30" fill="none" stroke="#1a1a1a" stroke-width="1.5"><path d="M0 1 H112 L94 15 L112 29 H0" fill="#fff"/></svg>
      <span>Homework</span>
    </div>
    <div class="hw-list">
      <div class="hw-entry"><div class="row"><span class="checkbox"></span><span class="label">Subject:</span></div><div class="line" style="top:23px"></div><div class="line" style="top:36px"></div><div class="task label">Task:</div><div class="line" style="top:64px"></div><div class="line" style="top:78px"></div></div>
      <div class="hw-entry"><div class="row"><span class="checkbox"></span><span class="label">Subject:</span></div><div class="line" style="top:23px"></div><div class="line" style="top:36px"></div><div class="task label">Task:</div><div class="line" style="top:64px"></div><div class="line" style="top:78px"></div></div>
      <div class="hw-entry"><div class="row"><span class="checkbox"></span><span class="label">Subject:</span></div><div class="line" style="top:23px"></div><div class="line" style="top:36px"></div><div class="task label">Task:</div><div class="line" style="top:64px"></div><div class="line" style="top:78px"></div></div>
      <div class="hw-entry"><div class="row"><span class="checkbox"></span><span class="label">Subject:</span></div><div class="line" style="top:23px"></div><div class="line" style="top:36px"></div><div class="task label">Task:</div><div class="line" style="top:64px"></div><div class="line" style="top:78px"></div></div>
      <div class="hw-entry"><div class="row"><span class="checkbox"></span><span class="label">Subject:</span></div><div class="line" style="top:23px"></div><div class="line" style="top:36px"></div><div class="task label">Task:</div><div class="line" style="top:64px"></div><div class="line" style="top:78px"></div></div>
      <div class="hw-entry"><div class="row"><span class="checkbox"></span><span class="label">Subject:</span></div><div class="line" style="top:23px"></div><div class="line" style="top:36px"></div><div class="task label">Task:</div><div class="line" style="top:64px"></div><div class="line" style="top:78px"></div></div>
      <div class="hw-entry"><div class="row"><span class="checkbox"></span><span class="label">Subject:</span></div><div class="line" style="top:23px"></div><div class="line" style="top:36px"></div><div class="task label">Task:</div><div class="line" style="top:64px"></div><div class="line" style="top:78px"></div></div>
    </div>
  </section>

  <!-- Assessments -->
  <section class="column assessments">
    <div class="column-tab label">
      <svg viewBox="0 0 96 30" fill="none" stroke="#1a1a1a" stroke-width="1.5"><path d="M0 1 H96 L78 15 L96 29 H0" fill="#fff"/></svg>
      <span>Assessments</span>
    </div>
    <div class="as-list">
      <div class="as-entry"><div class="row"><span class="checkbox"></span><span class="label">Assessment:</span><span class="fill"></span><span class="label">Due: __/__/__</span></div><div class="element label">Element:</div><div class="line" style="top:36px"></div><div class="line" style="top:50px"></div></div>
      <div class="as-entry"><div class="row"><span class="checkbox"></span><span class="label">Assessment:</span><span class="fill"></span><span class="label">Due: __/__/__</span></div><div class="element label">Element:</div><div class="line" style="top:36px"></div><div class="line" style="top:50px"></div></div>
      <div class="as-entry"><div class="row"><span class="checkbox"></span><span class="label">Assessment:</span><span class="fill"></span><span class="label">Due: __/__/__</span></div><div class="element label">Element:</div><div class="line" style="top:36px"></div><div class="line" style="top:50px"></div></div>
      <div class="as-entry"><div class="row"><span class="checkbox"></span><span class="label">Assessment:</span><span class="fill"></span><span class="label">Due: __/__/__</span></div><div class="element label">Element:</div><div class="line" style="top:36px"></div><div class="line" style="top:50px"></div></div>
      <div class="as-entry"><div class="row"><span class="checkbox"></span><span class="label">Assessment:</span><span class="fill"></span><span class="label">Due: __/__/__</span></div><div class="element label">Element:</div><div class="line" style="top:36px"></div><div class="line" style="top:50px"></div></div>
      <div class="as-entry"><div class="row"><span class="checkbox"></span><span class="label">Assessment:</span><span class="fill"></span><span class="label">Due: __/__/__</span></div><div class="element label">Element:</div><div class="line" style="top:36px"></div><div class="line" style="top:50px"></div></div>
      <div class="as-entry"><div class="row"><span class="checkbox"></span><span class="label">Assessment:</span><span class="fill"></span><span class="label">Due: __/__/__</span></div><div class="element label">Element:</div><div class="line" style="top:36px"></div><div class="line" style="top:50px"></div></div>
      <div class="as-entry"><div class="row"><span class="checkbox"></span><span class="label">Assessment:</span><span class="fill"></span><span class="label">Due: __/__/__</span></div><div class="element label">Element:</div><div class="line" style="top:36px"></div><div class="line" style="top:50px"></div></div>
      <div class="as-entry"><div class="row"><span class="checkbox"></span><span class="label">Assessment:</span><span class="fill"></span><span class="label">Due: __/__/__</span></div><div class="element label">Element:</div><div class="line" style="top:36px"></div><div class="line" style="top:50px"></div></div>
      <div class="as-entry"><div class="row"><span class="checkbox"></span><span class="label">Assessment:</span><span class="fill"></span><span class="label">Due: __/__/__</span></div><div class="element label">Element:</div><div class="line" style="top:36px"></div><div class="line" style="top:50px"></div></div>
    </div>
  </section>

</body>
</html>
```